Yogurt product needs a simple yet striking packaging.

We need a packaging for our yogurt product based in Singapore and Malaysia that is to be retailed in supermarkets. The brand of the yogurt is called ruò which means cow in mandarin. The details of our yogurt is as follows: Indian style all natural yogurt, plain in flavor. Its consistency is thick and creamy. It is preservative free and sugar free. We would like to see simple yet striking designs.

The packaging would be printed on a 200ml plastic cup (silk screen printing). The dimension for the cup is 235mm (w) x 69mm (h).

UPDATE:
We would be selecting 2 designs (First place and Second place) for this contest

Target Market(s)

Consumers who purchase yogurt.

Industry/Entity Type

Product

Requirements
Must have
• We would require some form of an artwork/picture that depicts a plain yogurt. It could be on a spoon, in a bowl, or a close up just on its own.
• UPDATED:
• The following texts are needed to be displayed on the package:
• 1. 'Indian style all natural yogurt' (Indian style could be subtle while all natural yogurt is highlighted as the main text).
• 2. 'Plain' (The flavor of the yogurt).
• 3. 'No Preservatives' and 'No Sugar Added' (Additional description about the yogurt).
• 4. The 2 certifications attached in the brief (Halal and Tarvo).
• 5. 'Ingredients: Water, milk solids, live and active cultures' (Ingredients for the yogurt).
• 6. 'Refrigerate below 4°C', 'Do not accept if seal is broken' and '200ml' (Additional contents required in the packaging).
• 7. Nutritional information, place of manufacture and product bar code which are attached in this brief.
Nice to have
• We would like the designers to have the freedom to create designs to their interest and ability, although we really love the designs from yogurt brands like Velandi and Brono's.

```html
<!DOCTYPE html>
<html lang="en">
<head>
<meta charset="utf-8">
<title>ruò Plain Yogurt – Cup Label</title>
<link rel="stylesheet" href="https://fonts.googleapis.com/css2?family=Arvo:wght@700&family=Oswald:wght@700&family=Pinyon+Script&family=Raleway:wght@300;800&family=Rokkitt:wght@400;700&display=swap">
<style>
  :root {
    --paper: #ffffff;
    --silver-light: #f4f4f4;
    --silver-mid: #dcdcdc;
    --silver-dark: #c4c4c4;
    --caramel: #a37a52;
    --caramel-dark: #7d5a38;
    --caramel-light: #c29a70;
    --ink: #1e1e1e;
    --cream: #fdf9f0;
    --yogurt: #ece9df;
  }
  * { margin: 0; padding: 0; box-sizing: border-box; }
  html, body { width: 967px; height: 1200px; overflow: hidden; background: var(--paper); }
  .canvas { position: relative; width: 967px; height: 1200px; }

  .label {
    position: absolute; left: 142px; top: 250px; width: 669px; height: 708px;
    background: linear-gradient(90deg, var(--silver-dark) 0%, var(--silver-light) 22%, var(--silver-mid) 55%, var(--silver-light) 78%, var(--silver-dark) 100%);
  }
  .lid-rim {
    position: absolute; left: 122px; top: 237px; width: 722px; height: 18px;
    background: var(--caramel);
  }
  .claims-band {
    position: absolute; left: 151px; top: 328px; width: 639px; height: 65px;
    background: linear-gradient(90deg, var(--caramel-dark), var(--caramel-light) 50%, var(--caramel-dark));
    display: flex; align-items: center; justify-content: space-evenly;
    font-family: "Rokkitt", serif; font-size: 46px; color: var(--cream); line-height: 1;
  }
  .claims-band b { font-weight: 700; }

  .brand-name {
    position: absolute; left: 276px; top: 420px; width: 345px;
    font-family: "Raleway", sans-serif; font-weight: 800; font-size: 132px;
    line-height: 1; color: var(--ink); letter-spacing: 2px;
  }
  .style-note {
    position: absolute; left: 628px; top: 455px;
    font-family: "Pinyon Script", cursive; font-size: 38px; line-height: 0.95; color: var(--ink);
  }
  .product-line {
    position: absolute; left: 242px; top: 563px;
    font-size: 48px; line-height: 1; color: var(--ink); white-space: nowrap;
  }
  .product-line .natural { font-family: "Raleway", sans-serif; font-weight: 300; letter-spacing: 1px; }
  .product-line .type { font-family: "Arvo", serif; font-weight: 700; margin-left: 10px; }

  .spoon-visual {
    position: absolute; left: 262px; top: 642px; width: 410px; height: 275px;
    background: radial-gradient(ellipse at 62% 70%, var(--yogurt) 0%, #d2d2d2 45%, rgba(200,200,200,0) 72%);
    border-radius: 50%;
  }
  .texture-ribbon { position: absolute; left: 290px; top: 620px; width: 435px; height: 142px; }
  .ribbon-text {
    position: absolute; left: 393px; top: 665px;
    font-family: "Oswald", sans-serif; font-weight: 700; font-size: 36px; color: var(--cream);
    transform: rotate(-6deg); transform-origin: left center; white-space: nowrap;
  }
  .flavour {
    position: absolute; left: 265px; top: 748px;
    font-family: "Arvo", serif; font-weight: 700; font-size: 48px; color: var(--ink);
  }
</style>
</head>
<body>
<main class="canvas">
  <div class="lid-rim"></div>
  <section class="label">
  </section>
  <div class="claims-band">
    <span>Preservative<b>FREE</b></span>
    <span>Sugar<b>FREE</b></span>
  </div>

  <h1 class="brand-name">ruò</h1>
  <p class="style-note">Indian<br>&nbsp;style</p>
  <p class="product-line"><span class="natural">ALL NATURAL</span><span class="type">YOGURT</span></p>

  <div class="spoon-visual" role="img" aria-label="Spoonful of thick plain white yogurt on a silver spoon"></div>

  <svg class="texture-ribbon" viewBox="0 0 435 142" aria-hidden="true">
    <polygon points="0,90 40,60 40,130" fill="var(--caramel-dark)"/>
    <polygon points="30,62 400,10 380,55 420,120 50,135" fill="var(--caramel)"/>
    <polygon points="360,14 435,0 405,60 435,110 380,125" fill="var(--caramel-dark)"/>
  </svg>
  <p class="ribbon-text">Thick and Creamy</p>

  <p class="flavour">Plain</p>
</main>
</body>
</html>
```